QR-482 Horizons, LLC business cards
Personal Fitness Training
Professional
QR 482 Horizons, LLC
Fitness Solutions
based out of Miami but want to train internationally over the net
bellamorvain@qr482.net
www.qr482.net
K20000047153
I would also like to list my bellamorvain@zentmail.net email
I will be based out of the Miami area but do not have an exact location for the address.
Contact for your Free Fitness Assessment
415 263 9071 or bellamorvain@qr482.net

```html
<!DOCTYPE html>
<html lang="en">
<head>
<meta charset="utf-8">
<title>QR-482 Horizons, LLC business cards</title>
<link href="https://fonts.googleapis.com/css2?family=Arimo:ital,wght@0,400;0,700;1,400;1,700&display=swap" rel="stylesheet">
<style>
  :root {
    --sheet: #d3d3d4;
    --card-light: #ffffff;
    --card-dark: #000000;
    --blue: #2d9fd9;
    --red: #d8262c;
    --ink: #3b3b3b;
    --muted: #5a5a5a;
    --silver: #c9c9c9;
  }
  * { margin: 0; padding: 0; box-sizing: border-box; }
  html, body { width: 1200px; height: 901px; overflow: hidden; }
  body { background: var(--sheet); font-family: "Arimo", Arial, sans-serif; position: relative; }

  .card { position: absolute; width: 572px; height: 333px; overflow: hidden; }
  .card--front { background: var(--card-light); top: 110px; }
  .card--back { background: var(--card-dark); top: 462px; height: 329px; }
  .card--left { left: 12px; }
  .card--right { left: 613px; }
  .theme-blue { --accent: var(--blue); }
  .theme-red { --accent: var(--red); }

  .brand { position: absolute; display: flex; align-items: center; gap: 12px; }
  .brand__square { width: 34px; height: 34px; background: var(--accent); }
  .brand__name { font-weight: 700; font-size: 48px; color: var(--ink); letter-spacing: 1px; }
  .card--front .brand { left: 22px; top: 38px; }
  .card--back .brand { left: 50%; top: 96px; transform: translateX(-50%); }
  .card--back .brand__name { color: var(--silver); font-size: 56px; }
  .card--back .brand__square { width: 40px; height: 40px; }

  .service { position: absolute; right: 16px; top: 64px; font-weight: 700; font-style: italic; font-size: 25px; color: var(--accent); }
  .rule { position: absolute; height: 2px; background: linear-gradient(to right, transparent, var(--accent) 30%, var(--accent)); }
  .rule--title { left: 240px; right: 12px; top: 104px; }
  .rule--foot-a { left: 0; right: 0; top: 289px; height: 2px; background: linear-gradient(to right, var(--accent), var(--accent) 70%, transparent); }
  .rule--foot-b { left: 20px; right: 0; top: 295px; height: 2px; opacity: .6; }

  .person { position: absolute; right: 22px; top: 150px; font-style: italic; font-size: 26px; color: var(--accent); }
  .tagline { position: absolute; right: 22px; top: 184px; font-size: 14px; color: var(--muted); }
  .details { position: absolute; left: 16px; top: 206px; font-size: 16px; line-height: 24px; color: var(--muted); list-style: none; }
  .email { position: absolute; top: 304px; font-size: 16px; color: var(--muted); }
  .email--work { left: 16px; }
  .email--personal { right: 12px; }

  .offer { position: absolute; left: 0; right: 0; text-align: center; color: #ffffff; }
  .offer__title { top: 226px; font-size: 19px; }
  .offer__contact { top: 252px; font-size: 16px; }
</style>
</head>
<body>

<section class="card card--front card--left theme-blue">
  <div class="brand"><span class="brand__square"></span><span class="brand__name">QR-482</span></div>
  <h2 class="service">Personal Fitness Training</h2>
  <div class="rule rule--title"></div>
  <p class="person">Bella Morvain</p>
  <p class="tagline">Look Better...Feel Better...Perform Better...</p>
  <ul class="details">
    <li>Phone: 415 263 9071</li>
    <li>License No. K20000047153</li>
    <li>Website: www.qr482.net</li>
  </ul>
  <div class="rule rule--foot-a"></div>
  <div class="rule rule--foot-b"></div>
  <p class="email email--work">Email: bellamorvain@qr482.net</p>
  <p class="email email--personal">bellamorvain@zentmail.net</p>
</section>

<section class="card card--front card--right theme-red">
  <div class="brand"><span class="brand__square"></span><span class="brand__name">QR-482</span></div>
  <h2 class="service">Personal Fitness Training</h2>
  <div class="rule rule--title"></div>
  <p class="person">Bella Morvain</p>
  <p class="tagline">Look Better...Feel Better...Perform Better...</p>
  <ul class="details">
    <li>Phone: 415 263 9071</li>
    <li>License No. K20000047153</li>
    <li>Website: www.qr482.net</li>
  </ul>
  <div class="rule rule--foot-a"></div>
  <div class="rule rule--foot-b"></div>
  <p class="email email--work">Email: bellamorvain@qr482.net</p>
  <p class="email email--personal">bellamorvain@zentmail.net</p>
</section>

<section class="card card--back card--left theme-blue">
  <div class="brand"><span class="brand__square"></span><span class="brand__name">QR-482</span></div>
  <p class="offer offer__title">Contact for your Free Fitness Assessment</p>
  <p class="offer offer__contact">415 263 9071 :: bellamorvain@qr482.net</p>
</section>

<section class="card card--back card--right theme-red">
  <div class="brand"><span class="brand__square"></span><span class="brand__name">QR-482</span></div>
  <p class="offer offer__title">Contact for your Free Fitness Assessment</p>
  <p class="offer offer__contact">415 263 9071 :: bellamorvain@qr482.net</p>
</section>

</body>
</html>
```